Internal windows + 2 internal walls

Hi Tobin, I need some designs for the front door and windows of our clinic, and some internal walls.

I have attached a picture of the front door and windows.
On them it needs
Sports Medicine
Pain Medicine
9371 6200
www.quillmereclinic.com.au
Maybe the logo.

I will get it printed as stickers. Can you keep the blues, the font, and the Hexagon thing going.

I have also included 2 walls that I am thinking I would put a graphic on. One is behind the desk directly facing the front door/windows, the other is off to the right.

For the wall facing the door, maybe we have the Logo on it

For the other wall, maybe we put "Pain is a thief. Take back what's yours" in the cursive you have done before

See what you can magic up for me.

Cheers

Rex

```html
<!DOCTYPE html>
<html lang="en">
<head>
<meta charset="utf-8">
<title>Quillmere Clinic – Window and Wall Graphics</title>
<link rel="stylesheet" href="https://fonts.googleapis.com/css2?family=Teko:wght@500&family=Saira+Condensed:wght@500&family=Poppins:wght@500&display=swap">
<style>
  :root {
    --blue: #1456a8;
    --blue-light: #2565b5;
    --pale: #e8ecf4;
    --white: #ffffff;
    --guide: #b3b3b3;
  }
  html, body { margin: 0; padding: 0; overflow: hidden; }
  body { width: 1200px; height: 499px; background: var(--white); position: relative; font-family: "Teko", sans-serif; }

  .guide-line { position: absolute; border-color: var(--guide); border-style: dashed; border-width: 0; }
  .guide-line--vertical { border-left-width: 2px; left: 49px; top: 69px; height: 388px; }
  .guide-line--horizontal { border-top-width: 2px; top: 58px; }
  .guide-label { position: absolute; color: var(--guide); font-family: "Saira Condensed", sans-serif; font-size: 22px; line-height: 1; }
  .guide-label--windows { left: 33px; top: 262px; transform: translate(-50%, -50%) rotate(-90deg); white-space: nowrap; word-spacing: 8px; }
  .guide-label--wall { top: 30px; transform: translateX(-50%); }

  .panel { position: absolute; overflow: hidden; box-shadow: 2px 2px 3px rgba(0,0,0,0.25); }
  .panel--blue { background: linear-gradient(180deg, var(--blue-light) 0%, var(--blue) 30%, var(--blue) 70%, var(--blue-light) 100%); }
  .panel--light { background: linear-gradient(180deg, var(--pale) 0%, var(--white) 40%, var(--white) 70%, var(--pale) 100%); }
  .panel__pattern { position: absolute; inset: 0; }

  .window-panel { left: 66px; top: 69px; width: 194px; height: 389px; }
  .window-panel__name { position: absolute; left: 0; right: 0; top: 44px; text-align: center; color: var(--white); font-size: 27px; line-height: 0.95; }
  .window-panel__band { position: absolute; left: 0; right: 0; top: 140px; height: 75px; background: var(--white); }
  .window-panel__services { position: absolute; left: 21px; top: 148px; color: var(--blue); line-height: 0.85; }
  .window-panel__services span { display: block; }
  .service--sports { font-size: 31px; letter-spacing: -0.3px; }
  .service--pain { font-size: 38px; letter-spacing: -0.3px; }
  .window-panel__phone { position: absolute; left: 21px; top: 230px; display: flex; align-items: center; gap: 14px; color: var(--white); font-size: 38px; line-height: 1; }
  .window-panel__phone svg { width: 28px; height: 28px; margin-top: -6px; }
  .window-panel__web { position: absolute; left: 0; right: 0; top: 265px; text-align: center; color: var(--white); font-family: "Poppins", sans-serif; font-size: 9.6px; }

  .tagline-panel { width: 402px; height: 185px; }
  .tagline-panel--blue { left: 337px; top: 69px; }
  .tagline-panel--light { left: 342px; top: 271px; }
  .tagline { position: absolute; left: 43px; top: 51px; margin: 0; font-weight: 500; font-size: 40px; line-height: 47px; letter-spacing: -0.6px; }
  .tagline-panel--light .tagline { left: 38px; }
  .tagline-panel--blue .tagline { color: var(--white); }
  .tagline-panel--light .tagline { color: var(--blue); }

  .logo-panel { left: 763px; width: 403px; height: 185px; }
  .logo-panel--light { top: 66px; }
  .logo-panel--blue { top: 273px; }
  .logo-panel__name { position: absolute; left: 0; right: 0; top: 34px; text-align: center; font-size: 66px; line-height: 0.85; }
  .logo-panel--light .logo-panel__name { color: var(--blue); }
  .logo-panel--blue .logo-panel__name { color: var(--white); }
</style>
</head>
<body>
  <div class="guide-line guide-line--vertical"></div>
  <div class="guide-label guide-label--windows">Internal Windows</div>

  <div class="guide-line guide-line--horizontal" style="left:336px;width:404px"></div>
  <div class="guide-label guide-label--wall" style="left:538px">wall</div>
  <div class="guide-line guide-line--horizontal" style="left:763px;width:404px"></div>
  <div class="guide-label guide-label--wall" style="left:964px">wall</div>

  <section class="panel panel--blue window-panel">
    <div class="panel__pattern" role="img" aria-label="Faint hexagon pattern background"></div>
    <div class="window-panel__name">QUILLMERE<br>CLINIC</div>
    <div class="window-panel__band"></div>
    <div class="window-panel__services">
      <span class="service--sports">SPORTS MEDICINE</span>
      <span class="service--pain">PAIN MEDICINE</span>
    </div>
    <div class="window-panel__phone">
      <svg viewBox="0 0 24 24" aria-hidden="true"><path fill="#fff" d="M6.6 2.2c.6-.3 1.3-.1 1.6.5l2.1 3.9c.3.6.2 1.2-.3 1.6L8.4 9.5c1.1 2.6 3.4 4.9 6 6.1l1.3-1.6c.4-.5 1.1-.6 1.6-.3l3.9 2.1c.6.3.8 1 .5 1.6l-1.3 2.6c-.5 1-1.6 1.5-2.7 1.3C10.4 20 4 13.6 2.7 6.3c-.2-1.1.3-2.2 1.3-2.7z"/></svg>
      <span>9371 6200</span>
    </div>
    <div class="window-panel__web">www.quillmereclinic.com.au</div>
  </section>

  <section class="panel panel--blue tagline-panel tagline-panel--blue">
    <div class="panel__pattern" role="img" aria-label="Faint hexagon pattern background"></div>
    <p class="tagline">PAIN IS A THIEF.<br>TAKE BACK WHAT’S YOURS.</p>
  </section>

  <section class="panel panel--light tagline-panel tagline-panel--light">
    <div class="panel__pattern" role="img" aria-label="Faint hexagon pattern background"></div>
    <p class="tagline">PAIN IS A THIEF.<br>TAKE BACK WHAT’S YOURS.</p>
  </section>

  <section class="panel panel--light logo-panel logo-panel--light">
    <div class="panel__pattern" role="img" aria-label="Faint hexagon pattern background"></div>
    <div class="logo-panel__name">QUILLMERE<br>CLINIC</div>
  </section>

  <section class="panel panel--blue logo-panel logo-panel--blue">
    <div class="panel__pattern" role="img" aria-label="Faint hexagon pattern background"></div>
    <div class="logo-panel__name">QUILLMERE<br>CLINIC</div>
  </section>
</body>
</html>
```